Tesk Laptop Cover Skin for a DJ

I’m a wedding/corporate DJ that’s looking to have a unique laptop skin design for my Zentrix laptop.

I will like to have a laptop cover skin that is a creative combination of professional, uniqueness, timeliness and looks solid.

I will like someone to take my current logo to incorporate into the design and only change the bottom “Tagline” in the logo to my new tagline listed below in the same area as the current tag.
New Tag: DJ Services | Photo Booths | Event Lighting

3D Feel
½ of laptop design with info list above and ½ laptop design with VTK attached logo
Colors: Stick with colors in my logo
Professional Design
o Note: I used this laptop for meetings and for DJ Gigs
Fonts: Open
Company Colors: Maroon / white / black

I have added our logo as an attachment, as well as our current laptop design skin. We are looking for something totally different.

Additionally, I have attached a further description of what we will like included.

Requirements
Must have
• Name: DoRN HaLE ( Name need to be BIG but not over bearing ) Company Name: VTK Entertainment 2nd Co Name: VTK Management Website: www.vtkentertainment-example.net VTK Logo Attached: See attached file o Note: EPS or AI file format of the logo can be sent to winner of the design contest PW Name: MrVTK7000 Hashtag: #VTKEntertainment Chatterly Name: VTK Entertainment

```html
<!DOCTYPE html>
<html lang="en">
<head>
<meta charset="utf-8">
<title>DoRN HaLE – VTK Entertainment Laptop Skin</title>
<link href="https://fonts.googleapis.com/css2?family=Saira+Condensed:wght@400;500;600&display=swap" rel="stylesheet">
<style>
  :root {
    --maroon: #6e1a1c;
    --ink: #1d1d1d;
    --skin-light: #e4e4e5;
    --skin-dark: #cfcfd1;
    --backdrop: #f2f2f2;
    --muted: #4a4a4a;
  }
  * { margin: 0; padding: 0; box-sizing: border-box; }
  html, body {
    width: 1200px; height: 912px; overflow: hidden;
    background: var(--backdrop);
    font-family: "Saira Condensed", "Arial Narrow", sans-serif;
  }
  .skin {
    position: absolute; left: 0; top: 0; width: 1200px; height: 912px;
    border-radius: 28px;
    background: linear-gradient(160deg, var(--skin-light) 0%, #dadadb 55%, var(--skin-dark) 100%);
    overflow: hidden;
  }
  .owner-name {
    position: absolute; right: 440px; top: 150px;
    font-size: 118px; font-weight: 500; line-height: 1;
    color: var(--maroon); letter-spacing: 1px; white-space: nowrap;
  }
  .owner-companies {
    position: absolute; right: 434px; top: 284px;
    text-align: right; font-size: 24px; line-height: 1.3;
    color: var(--muted); white-space: nowrap;
  }
  .company-mark {
    position: absolute; left: 790px; top: 168px; width: 390px;
    display: flex; flex-direction: column; align-items: flex-start;
  }
  .company-mark__row { display: flex; align-items: center; gap: 14px; }
  .company-mark__dot {
    flex: none; width: 60px; height: 60px; border-radius: 50%;
    background: var(--maroon);
  }
  .company-mark__name {
    font-size: 44px; font-weight: 600; color: var(--maroon); line-height: 1;
    white-space: nowrap;
  }
  .company-mark__tagline {
    margin-top: 16px; font-size: 20px; color: var(--ink);
    white-space: nowrap;
  }
  .device-brand {
    position: absolute; left: 0; width: 1200px; top: 345px;
    text-align: center; font-size: 38px; font-weight: 500;
    color: #f7f7f7;
  }
  .music-band {
    position: absolute; left: 50px; top: 410px; width: 1100px; height: 290px;
    border-radius: 140px 60px 60px 140px;
    background: linear-gradient(90deg,
      #e5c23a 0%, #c9306a 10%, #2e6cc4 20%, #9a3fb0 35%,
      #e7a33a 50%, #7a48c4 62%, #e08a3a 75%, #3f8fd0 88%, #e6c74a 100%);
    opacity: 0.8;
  }
  .contact-row {
    position: absolute; left: 50px; right: 50px; top: 790px;
    display: flex; align-items: center; justify-content: space-between;
    color: var(--ink); font-size: 22px; white-space: nowrap;
  }
  .contact-item { display: flex; align-items: center; gap: 10px; white-space: nowrap; }
  .contact-badge {
    flex: none; width: 36px; height: 36px; border-radius: 50%;
    background: var(--maroon); color: #fff;
    display: flex; align-items: center; justify-content: center;
    font-size: 20px; font-weight: 600;
  }
  .contact-label { color: var(--maroon); font-weight: 500; }
  .contact-url { color: var(--maroon); font-size: 26px; }
</style>
</head>
<body>
  <main class="skin">
    <h1 class="owner-name">DoRN HaLE</h1>
    <p class="owner-companies">VTK Entertainment<br>VTK Management</p>

    <div class="company-mark">
      <div class="company-mark__row">
        <span class="company-mark__dot"></span>
        <span class="company-mark__name">VTK Entertainment</span>
      </div>
      <p class="company-mark__tagline">DJ Services | Photo Booths | Event Lighting</p>
    </div>

    <div class="device-brand">Tesk</div>

    <div class="music-band" role="img" aria-label="Watercolour splash of colourful music notes and treble clefs flowing along a staff"></div>

    <footer class="contact-row">
      <span class="contact-item">MrVTK7000</span>
      <span class="contact-item"><span class="contact-badge"></span><span class="contact-label">PW</span></span>
      <span class="contact-item">#VTKEntertainment</span>
      <span class="contact-item"><span class="contact-badge">#</span></span>
      <span class="contact-item">VTK Entertainment</span>
      <span class="contact-item"><span class="contact-badge"></span><span class="contact-label">Chatterly</span></span>
      <span class="contact-item contact-url">www.vtkentertainment-example.net</span>
    </footer>
  </main>
</body>
</html>
```